Real Estate Brokerage - Sales Promo Flyer

We would like someone to design a 8x11 high gloss promotional flyer for our real estate agents to use in the field when presenting to a possible listing client (someone who wants to sell their home).

The flyer should include some of our brokerage's recent sales transaction numbers, as well as benefits to using our service.

We would like our design to have a professional appeal, with bold colors, and vivid images.

I have attached 5 images of recently sold homes:
247 Marisol Lane Trust, Palm Beach Gardens, Florida - Sold for $424,000
4718 Tierra Linda Ct, Boca Raton, FL 33431 - Sold for $415,000
418 Verbena Hills Drive, Palm Beach Gardens, Florida - Sold for $877,500
20417 Heron Bluff Circle, West Palm Beach, Florida - Sold for $380,000
382 Thistle Road, Greenacres, Florida - Sold for $234,500

I can provide any additional details you need. See attached files.
Updates

This flyer should contain our business name, logo, phone numbers, and website (however you see fit). PelicoHomes Palm Beach County | (561) 402-1186 Broward County | (954) 238-4417 www.pelicohomes-example.com

More Properties to Add: 418 Verbena Hills Drive, Palm Beach Gardens, Florida - Sold for $877,500 20417 Heron Bluff Circle, West Palm Beach, Florida - Sold for $380,000 382 Thistle Road, Greenacres, Florida - Sold for $234,500

I have added the Original Logo Images. Please use one of these in your design.

I have uploaded an image of our syndication partners, please add this to your flyers.

Please submit all of your Design. Thanks!

Please submit your edits

Industry/Entity Type

Real Estate

Requirements
Must have
• PelicoHomes is one word with a capital K and capital R.

Must have website and phone number.

PelicoHomes
www.pelicohomes-example.com
561-402-1186 - Palm Beach County
954-238-4417 - Broward County

```html
<!DOCTYPE html>
<html lang="en">
<head>
<meta charset="utf-8">
<title>PelicoHomes – Recent Sales Flyer</title>
<link rel="stylesheet" href="https://fonts.googleapis.com/css2?family=Cinzel:wght@500&family=Lato:ital,wght@0,400;0,700;1,400&family=Oswald:wght@500;600&display=swap">
<style>
  :root {
    --paper: #f1f1f2;
    --ink: #4a4a4a;
    --ink-soft: #666;
    --blue-deep: #0a78b8;
    --blue-mid: #1598d4;
    --blue-bright: #2bb3e6;
    --teal: #1fa8d2;
    --teal-dark: #1a90c4;
    --white: #ffffff;
    --sky: #cfe2f1;
    --stucco: #d9c89a;
    --lawn: #5f8f3e;
  }
  * { margin: 0; padding: 0; box-sizing: border-box; }
  html, body { width: 933px; height: 1200px; overflow: hidden; background: var(--paper); }
  .flyer { position: relative; width: 933px; height: 1200px; background: var(--paper); font-family: "Lato", sans-serif; overflow: hidden; }

  .masthead { position: absolute; top: 0; left: 0; width: 100%; height: 109px; display: flex; align-items: center; justify-content: center; gap: 14px; }
  .brand-dot { width: 34px; height: 34px; border-radius: 50%; background: var(--teal); }
  .brand-name { font-family: "Cinzel", serif; font-weight: 500; font-size: 26px; letter-spacing: 3px; color: var(--ink); }
  .top-rule { position: absolute; top: 109px; left: 0; width: 100%; height: 12px; background: var(--blue-bright); }

  .hero-photo { position: absolute; top: 121px; left: 0; width: 100%; height: 500px;
    background: linear-gradient(180deg, var(--sky) 0%, #e8eef3 30%, var(--stucco) 55%, #c9b784 75%, var(--lawn) 100%); }

  .sales-panel { position: absolute; top: 560px; left: 0; width: 933px; height: 500px; }

  .feature-banner { position: absolute; top: 593px; left: 153px; width: 628px; height: 114px; display: flex; filter: drop-shadow(0 4px 6px rgba(0,0,0,.25)); }
  .feature-address { width: 385px; background: var(--teal-dark); color: var(--white); padding: 22px 0 0 26px; }
  .feature-street { font-weight: 700; font-size: 31px; line-height: 1.1; white-space: nowrap; }
  .feature-city { font-size: 19px; margin-top: 4px; }
  .feature-price { flex: 1; background: var(--teal); color: var(--white); text-align: center; padding-top: 14px; clip-path: polygon(0 0, 92% 0, 100% 22%, 100% 100%, 0 100%); }
  .feature-price-label { font-weight: 700; font-size: 28px; }
  .feature-price-value { font-size: 42px; line-height: 1.05; }

  .recent-heading { position: absolute; top: 724px; left: 0; width: 100%; display: flex; align-items: center; justify-content: center; gap: 10px; color: var(--white); font-style: italic; font-weight: 400; font-size: 25px; }
  .recent-heading::before, .recent-heading::after { content: ""; width: 90px; height: 2px; background: var(--white); }

  .recent-sales { position: absolute; top: 780px; left: 0; width: 100%; }
  .sale-card { position: absolute; width: 193px; text-align: center; color: var(--white); }
  .sale-photo { width: 193px; height: 130px; border: 5px solid var(--white); box-shadow: 0 3px 6px rgba(0,0,0,.3);
    background: linear-gradient(180deg, #bcd6ea 0%, #e3e6e2 35%, #cdbf9c 55%, #6f9a4c 75%, #4d7e35 100%); }
  .sale-street { font-family: "Oswald", sans-serif; font-weight: 600; font-size: 18px; text-transform: uppercase; margin-top: 14px; white-space: nowrap; letter-spacing: -.5px; }
  .sale-city { font-size: 14px; margin-top: 1px; }
  .sale-price { display: inline-flex; align-items: center; gap: 8px; margin-top: 6px; }
  .sale-pill { background: var(--teal); font-style: italic; font-size: 12px; padding: 3px 14px; }
  .tick { width: 14px; height: 14px; }

  .bottom-rule { position: absolute; top: 1047px; left: 0; width: 100%; height: 9px; background: var(--blue-bright); }

  .contact-bar { position: absolute; top: 1056px; left: 0; width: 100%; height: 144px; }
  .call-now { position: absolute; left: 44px; top: 24px; width: 215px; font-family: "Oswald", sans-serif; font-weight: 500; font-size: 40px; line-height: 1; color: var(--ink); letter-spacing: -1.5px; white-space: nowrap; }
  .contact-lines { position: absolute; left: 277px; top: 12px; font-size: 19px; line-height: 29px; color: var(--ink-soft); white-space: nowrap; }
  .contact-lines .web { color: var(--ink); padding-left: 4px; }
  .badge { position: absolute; top: 34px; background: var(--ink); }
  .badge-one { left: 714px; width: 40px; height: 44px; }
  .badge-two { left: 796px; width: 44px; height: 40px; border-radius: 4px; }
</style>
</head>
<body>
<main class="flyer">
  <header class="masthead">
    <span class="brand-dot"></span>
    <span class="brand-name">PelicoHomes</span>
  </header>
  <div class="top-rule"></div>

  <div class="hero-photo" role="img" aria-label="Photo of a two-storey Mediterranean-style home with palm trees and a paver driveway"></div>

  <svg class="sales-panel" viewBox="0 0 933 500" preserveAspectRatio="none" aria-hidden="true">
    <defs>
      <linearGradient id="panelFill" x1="0" y1="0" x2="0" y2="1">
        <stop offset="0" stop-color="#2fb6e8"/>
        <stop offset="0.5" stop-color="#1598d4"/>
        <stop offset="1" stop-color="#0a78b8"/>
      </linearGradient>
    </defs>
    <path d="M0 18 Q466 80 933 10 L933 500 L0 500 Z" fill="#bfe6f6"/>
    <path d="M0 30 Q466 92 933 22 L933 500 L0 500 Z" fill="url(#panelFill)"/>
  </svg>

  <section class="feature-banner">
    <div class="feature-address">
      <div class="feature-street">418 Verbena Hills Drive,</div>
      <div class="feature-city">Palm Beach Gardens, Florida</div>
    </div>
    <div class="feature-price">
      <div class="feature-price-label">Sold for</div>
      <div class="feature-price-value">$877,500</div>
    </div>
  </section>

  <h2 class="recent-heading">Others Recent Sales</h2>

  <section class="recent-sales">
    <article class="sale-card" style="left:39px">
      <div class="sale-photo" role="img" aria-label="Photo of a single-storey home with palms and lawn"></div>
      <div class="sale-street">247 Marisol Lane Trust,</div>
      <div class="sale-city">Palm Beach Gardens, Florida</div>
      <div class="sale-price"><span class="sale-pill">Sold for $424,000</span>
        <svg class="tick" viewBox="0 0 14 14"><path d="M2 7 L6 11 L12 3" fill="none" stroke="#6fd0f2" stroke-width="2"/></svg></div>
    </article>
    <article class="sale-card" style="left:267px">
      <div class="sale-photo" role="img" aria-label="Photo of a ranch home with a wide lawn and driveway"></div>
      <div class="sale-street">20417 Heron Bluff Circle</div>
      <div class="sale-city">West Palm Beach, Florida</div>
      <div class="sale-price"><span class="sale-pill">Sold for $380,000</span>
        <svg class="tick" viewBox="0 0 14 14"><path d="M2 7 L6 11 L12 3" fill="none" stroke="#6fd0f2" stroke-width="2"/></svg></div>
    </article>
    <article class="sale-card" style="left:486px">
      <div class="sale-photo" role="img" aria-label="Photo of a grey home with garage and shrubs"></div>
      <div class="sale-street">382 Thistle Road</div>
      <div class="sale-city">Greenacres, Florida</div>
      <div class="sale-price"><span class="sale-pill">Sold for $234,500</span>
        <svg class="tick" viewBox="0 0 14 14"><path d="M2 7 L6 11 L12 3" fill="none" stroke="#6fd0f2" stroke-width="2"/></svg></div>
    </article>
    <article class="sale-card" style="left:702px">
      <div class="sale-photo" role="img" aria-label="Photo of a home behind a large shade tree"></div>
      <div class="sale-street">4718 Tierra Linda Ct</div>
      <div class="sale-city">Boca Raton, Florida</div>
      <div class="sale-price"><span class="sale-pill">Sold for $415,000</span>
        <svg class="tick" viewBox="0 0 14 14"><path d="M2 7 L6 11 L12 3" fill="none" stroke="#6fd0f2" stroke-width="2"/></svg></div>
    </article>
  </section>

  <div class="bottom-rule"></div>

  <footer class="contact-bar">
    <div class="call-now">CALL US NOW:</div>
    <div class="contact-lines">
      <div>(561) 402-1186 | Palm Beach County</div>
      <div>(954) 238-4417 | Broward County</div>
      <div class="web">www.pelicohomes-example.com</div>
    </div>
    <span class="badge badge-one" aria-label="Association badge"></span>
    <span class="badge badge-two" aria-label="Housing badge"></span>
  </footer>
</main>
</body>
</html>
```